Fernvale Craft Works business card design- Fine Art sculpture business (Contract guaranteed)

This business card is for a fine art business. Though we don't have a website up and running yet it should be up soon. I would like the business card to be elegant and fairly simple with a picture of one of my sculptures on the front (you might need to photoshop out the background) as well as my basic contact info (my name,phone # and e-mail). On the back I'd like it to be pretty simple with just "Notes" and some blank lines for writing in info.

Target Market(s)

High end artwork buyers

Industry/Entity Type

Art Gallery

Contact Information for Business Card

Marlo Prewitt Phone: (555) 213-4098 E-mail: marlo@quillbrookmail.com Facebook: @fernvalecraftworks Instagram: fernvalecraftworks

Colors

Designer to choose colors to be used in the design.

Requirements
Must have
• *A picture of one of my sculptures*, my name, business name (Fernvale Craft Works), e-mail, phone #, and a notes section on the back.
• Fernvale Craft Works
• Marlo Prewitt
• (555)213-4098
• marlo@quillbrookmail.com
• Facebook: @fernvalecraftworks
• Instagram: fernvalecraftworks
Nice to have
• It'd be nice if you can crop out the background in the sculpture pictures, which ever one you end up using.

```html
<!DOCTYPE html>
<html lang="en">
<head>
<meta charset="utf-8">
<title>Fernvale Craft Works – Business Card</title>
<link rel="stylesheet" href="https://fonts.googleapis.com/css2?family=Spectral:wght@400&display=swap">
<style>
  :root {
    --backdrop: #8b7045;
    --backdrop-light: #a89677;
    --card: #ffffff;
    --ink: #1c1c1c;
    --studio-brown: #6b4a1c;
    --divider: #a88b62;
    --rule: #cfcfcf;
    --icon: #444444;
    --stone-deep: #3d2466;
    --stone-mid: #6a3fa0;
    --stone-base: #5b5f66;
  }
  * { margin: 0; padding: 0; box-sizing: border-box; }
  html, body { width: 1000px; height: 1200px; overflow: hidden; }
  body {
    position: relative;
    background: var(--backdrop);
    font-family: "Spectral", Georgia, serif;
    color: var(--ink);
  }
  .backdrop-corner { position: absolute; left: 0; top: 0; }
  .card {
    position: absolute;
    left: 128px;
    width: 782px;
    height: 447px;
    background: var(--card);
    box-shadow: 0 6px 16px rgba(0,0,0,0.22);
  }
  .card-front { top: 123px; }
  .card-back { top: 635px; }

  .sculpture-photo {
    position: absolute;
    left: 140px; top: 82px;
    width: 190px; height: 260px;
    border-radius: 40% 40% 12% 12% / 30% 30% 8% 8%;
    background: radial-gradient(ellipse at 50% 40%, var(--stone-mid) 0%, var(--stone-deep) 60%, var(--stone-base) 100%);
  }
  .studio-name {
    position: absolute;
    left: 40px; width: 310px;
    top: 350px;
    text-align: center;
    font-size: 31px;
    color: var(--studio-brown);
    white-space: nowrap;
  }
  .divider {
    position: absolute;
    left: 363px; top: 123px;
    width: 2px; height: 196px;
    background: var(--divider);
  }
  .contact-block { position: absolute; left: 423px; top: 124px; }
  .person-name { font-size: 30px; line-height: 1; margin-bottom: 18px; white-space: nowrap; }
  .contact-list { list-style: none; }
  .contact-item {
    display: flex; align-items: center;
    height: 24px; margin-bottom: 14px;
    font-size: 19px; white-space: nowrap;
  }
  .contact-item:nth-child(2) { margin-bottom: 14px; }
  .contact-icon { width: 22px; height: 22px; margin-right: 10px; flex: none; }

  .notes-lines { position: absolute; left: 100px; top: 0; width: 595px; height: 100%; }
  .notes-line {
    position: absolute; left: 0; right: 0;
    border-top: 2px dotted var(--rule);
  }
</style>
</head>
<body>
  <svg class="backdrop-corner" width="1000" height="1200" aria-hidden="true">
    <polygon points="1000,712 1000,1200 525,1200" fill="var(--backdrop-light)"/>
  </svg>

  <section class="card card-front">
    <div class="sculpture-photo" role="img" aria-label="Photograph of an amethyst geode sculpture on a stone base"></div>
    <p class="studio-name">Fernvale Craft Works</p>
    <div class="divider"></div>
    <div class="contact-block">
      <h1 class="person-name" style="font-weight:400">Marlo Prewitt</h1>
      <ul class="contact-list">
        <li class="contact-item">
          <svg class="contact-icon" viewBox="0 0 22 22" aria-hidden="true">
            <rect x="5" y="1" width="12" height="20" rx="2" fill="none" stroke="var(--icon)" stroke-width="1.3"/>
            <line x1="5" y1="4.5" x2="17" y2="4.5" stroke="var(--icon)" stroke-width="1"/>
            <line x1="5" y1="17" x2="17" y2="17" stroke="var(--icon)" stroke-width="1"/>
            <line x1="9.5" y1="19" x2="12.5" y2="19" stroke="var(--icon)" stroke-width="1"/>
          </svg>
          (555) 213-4098
        </li>
        <li class="contact-item">
          <svg class="contact-icon" viewBox="0 0 22 22" aria-hidden="true">
            <text x="11" y="16" text-anchor="middle" font-family="Spectral, serif" font-size="18" fill="var(--icon)">@</text>
          </svg>
          marlo@quillbrookmail.com
        </li>
        <li class="contact-item">
          <svg class="contact-icon" viewBox="0 0 22 22" aria-hidden="true">
            <circle cx="11" cy="11" r="9.5" fill="none" stroke="var(--icon)" stroke-width="1.1"/>
          </svg>
          @fernvalecraftworks
        </li>
        <li class="contact-item">
          <svg class="contact-icon" viewBox="0 0 22 22" aria-hidden="true">
            <circle cx="11" cy="11" r="9.5" fill="none" stroke="var(--icon)" stroke-width="1.1"/>
          </svg>
          fernvalecraftworks
        </li>
      </ul>
    </div>
  </section>

  <section class="card card-back">
    <div class="notes-lines">
      <div class="notes-line" style="top:97px"></div>
      <div class="notes-line" style="top:162px"></div>
      <div class="notes-line" style="top:221px"></div>
      <div class="notes-line" style="top:286px"></div>
      <div class="notes-line" style="top:354px"></div>
    </div>
  </section>
</body>
</html>
```